Vantrell Law Letterhead

We need a new letterhead design for a Law Firm. The address for the law firm is 4817 Larkspur Boulevard, Suite 250, Houston, Texas 77342. Phone Number: 832-619-3057; Fax Number: 832-407-1694. The logo is uploaded to the project.

```html
<!DOCTYPE html>
<html lang="en">
<head>
<meta charset="utf-8">
<title>Vantrell Law Letterhead</title>
<link rel="stylesheet" href="https://fonts.googleapis.com/css2?family=Raleway:wght@400;700&family=Tinos&display=swap">
<style>
  :root {
    --backdrop: #ece4d6;
    --paper: #ffffff;
    --navy: #1f3266;
    --red: #e31e24;
    --ink: #2a2a2a;
    --muted: #555555;
  }
  * { margin: 0; padding: 0; box-sizing: border-box; }
  html, body { width: 1200px; height: 1200px; overflow: hidden; background: var(--backdrop); }
  .letterhead {
    position: absolute; left: 175px; top: 50px;
    width: 850px; height: 1100px;
    background: var(--paper);
    font-family: "Raleway", sans-serif;
    color: var(--ink);
  }
  .brand {
    position: absolute; top: 92px; left: 0; right: 0;
    display: flex; justify-content: center;
  }
  .brand-row { display: flex; align-items: center; gap: 16px; }
  .brand-mark { width: 44px; height: 44px; border-radius: 50%; background: var(--navy); }
  .brand-name {
    font-family: "Raleway", sans-serif; font-weight: 700;
    font-size: 40px; color: var(--navy); letter-spacing: 0.5px;
  }
  .sender {
    position: absolute; left: 70px; top: 262px;
    font-size: 11.5px; line-height: 1.35; font-style: normal;
  }
  .sender strong { font-weight: 700; display: block; }
  .sender .sender-phone { color: var(--muted); font-size: 13px; }
  .letter-body {
    position: absolute; left: 295px; top: 262px; width: 480px;
    font-size: 12.5px; line-height: 1.62; text-align: justify;
  }
  .salutation { font-weight: 700; margin-bottom: 16px; }
  .letter-body p { margin-bottom: 26px; }
  .signoff { font-size: 11.5px; line-height: 1.3; margin-top: 6px; }
  .signoff strong { display: block; font-weight: 700; }
  .signature {
    margin-top: 10px; margin-left: 90px;
    width: 130px; height: 48px; border-radius: 6px;
    background: linear-gradient(90deg, #f1f1f1, #e4e4e4);
  }
  .footer-bands { position: absolute; left: 0; right: 0; top: 960px; }
  .band { height: 14px; }
  .band-red { background: var(--red); }
  .band-navy { background: var(--navy); margin-top: 8px; }
  .footer-contact {
    position: absolute; left: 0; right: 0; top: 1010px;
    text-align: center; font-family: "Tinos", serif;
    font-size: 14px; color: var(--navy); word-spacing: 1px;
  }
  .footer-contact span { margin-left: 14px; }
</style>
</head>
<body>
  <main class="letterhead">
    <header class="brand">
      <div class="brand-row">
        <div class="brand-mark"></div>
        <div class="brand-name">Vantrell Law</div>
      </div>
    </header>

    <address class="sender">
      <strong>1185 Marlow Crest Lane</strong>
      <strong>Pasadena, CA 91106</strong>
      <span class="sender-phone">714-356-0192</span>
    </address>

    <article class="letter-body">
      <div class="salutation">Dear Mr. Castellan</div>
      <p>Fusce scelerisque sem sem, non interdum ligula gravida id. Curabitur sit amet molestie elit. Pellentesque ac congue diam. Duis varius suscipit elementum. Ut ac volutpat arcu, id commodo erat. Suspendisse tempor diam ut nunc egestas finibus. Maecenas quis porttitor dolor, a accumsan odio. Phasellus nisl metus, consectetur ut venenatis sit amet, imperdiet at nunc.</p>
      <p>Donec facilisis malesuada ipsum sit amet vulputate. Integer justo justo, fermentum vitae pellentesque feugiat, ullamcorper non velit. Suspendisse molestie volutpat nisl at faucibus. Praesent posuere sodales libero, sed lacinia lacus ultrices eu. Phasellus lobortis, lectus sit amet vehicula hendrerit, risus purus blandit nunc, porttitor dictum arcu nisl varius ipsum. Nam tempus et purus sit amet cursus. Ut nec mauris quam. Integer condimentum quis magna id tempus. Pellentesque et orci scelerisque nisi faucibus egestas et at orci. Aliquam placerat ultricies erat id tincidunt. Nunc quis justo ipsum. Pellentesque at nisl et nulla posuere sollicitudin vitae vel ex. Vivamus fermentum orci sem. Phasellus tempor, metus vitae rutrum varius, ex libero mattis sapien, nec dictum enim augue non augue. Vestibulum in orci ut augue iaculis porttitor.</p>
      <p>Praesent sit amet augue auctor, ultrices dui eget, pellentesque enim. Vivamus eu elementum odio. Nulla vitae enim porta, posuere tellus in, euismod nulla. Pellentesque vitae sodales ligula, vitae viverra nunc. Integer tristique sit amet leo vel feugiat.</p>
      <div class="signoff">
        <strong>Daniel R. Whitford</strong>
        Marketing Manager
      </div>
      <div class="signature" role="img" aria-label="Handwritten signature"></div>
    </article>

    <div class="footer-bands">
      <div class="band band-red"></div>
      <div class="band band-navy"></div>
    </div>
    <footer class="footer-contact">
      4817 Larkspur Boulevard, Suite 250, Houston, Texas 77342
      <span>Tel: 832-619-3057</span>
      <span>Fax: 832-407-1694</span>
    </footer>
  </main>
</body>
</html>
```